Solar panel installation company needs a flyer.

Need a double sided flyer (not sure what size at this stage) to attract new customers and engage them with our company. We supply and install solar panels for residential homes and want residents to see the sense in installing solar.
Ideally we need on the front page:
A photo of us installing solar panels so the customer can see the face of our business and who they are dealing with.
A question: "What will your electricity bill look like in 5 years time?"
An answer to the above question: "Install solar power today and start saving!" (with a picture of solar panels on roof and money underneath - see attached)
A section that says: "3 reasons to install solar..."
1 - "The sun provides ample amounts of free, clean energy every day."
2 - "The government provides generous incentives saving you thousands of $$."
3 - "Advanced technology allows you to store your energy and use it a night."
A call to action such as: "Call us now for a free quote." (Phone 0482 917 605).
Back page we need:
A simple table showing a price guide with original cost crossed out and discounted cost highlighted. And a section with more information under the table.
A section about our company with a picture of us.
A customer testimonial.
A footer section with more information such as business number, license numbers, website and terms of the price guide.
We want you to come up with creative, eye catching and easy to read ways to display the above information with enough white space so it doesn't seem too busy. We are open to other suggestions, colour scheme and amount of information that should be placed on the flyer.
We also need to display our website on both sides (www.tarnbrookservices.com.au)
Please find attached photos, logos and content for you to use in the best way possible.
If you feel images are not of quality we can arrange professional images to be taken and uploaded.
Home owners aged 30+
It Company

```html
<!DOCTYPE html>
<html lang="en">
<head>
<meta charset="UTF-8">
<title>Tarnbrook Solar &amp; Electrical – Flyer</title>
<link href="https://fonts.googleapis.com/css2?family=Montserrat:ital,wght@0,600;0,800;1,800&display=swap" rel="stylesheet">
<style>
  :root {
    --orange: #f47b20;
    --orange-deep: #e8661a;
    --white: #ffffff;
    --ink: #1f1f1f;
    --sky-top: #8fc4ec;
    --sky-low: #cfe4f4;
    --panel-dark: #1f3f7a;
    --panel-mid: #2f5fa8;
  }
  * { margin: 0; padding: 0; box-sizing: border-box; }
  html, body { width: 849px; height: 1200px; overflow: hidden; background: var(--white); }
  .flyer {
    position: relative;
    width: 849px;
    height: 1200px;
    overflow: hidden;
    background: var(--white);
    font-family: "Montserrat", Arial, sans-serif;
  }
  .brand {
    position: absolute;
    top: 40px;
    left: 0;
    width: 100%;
    display: flex;
    justify-content: center;
    align-items: center;
    gap: 18px;
  }
  .brand-dot {
    width: 74px;
    height: 74px;
    border-radius: 50%;
    background: var(--orange);
  }
  .brand-name {
    color: var(--orange);
    font-weight: 800;
    font-size: 34px;
    letter-spacing: 0.5px;
  }
  .hero-photo {
    position: absolute;
    top: 150px;
    left: 0;
    width: 849px;
    height: 580px;
    background:
      linear-gradient(160deg, transparent 0 42%, var(--panel-mid) 42% 70%, var(--panel-dark) 70%),
      linear-gradient(180deg, var(--sky-top), var(--sky-low));
  }
  .question-band {
    position: absolute;
    top: 640px;
    left: -40px;
    width: 930px;
    height: 140px;
    background: var(--orange);
    transform: rotate(-4deg);
    display: flex;
    align-items: center;
    justify-content: center;
    box-shadow: 0 4px 0 var(--orange-deep);
  }
  .question {
    color: var(--white);
    font-weight: 800;
    font-size: 42px;
    line-height: 1.12;
    text-align: center;
    text-transform: uppercase;
  }
  .reasons-title {
    position: absolute;
    top: 800px;
    width: 100%;
    text-align: center;
    color: var(--orange);
    font-weight: 800;
    font-size: 48px;
    text-transform: uppercase;
  }
  .reasons {
    position: absolute;
    top: 890px;
    left: 36px;
    list-style: none;
  }
  .reason {
    display: table;
    margin-bottom: 20px;
    padding: 10px 16px;
    background: var(--orange);
    color: var(--white);
    font-weight: 600;
    font-size: 16.5px;
    text-transform: uppercase;
  }
  .cta {
    position: absolute;
    top: 1094px;
    right: 36px;
    color: var(--orange);
    font-weight: 800;
    font-size: 28px;
    text-transform: uppercase;
  }
</style>
</head>
<body>
  <main class="flyer">
    <header class="brand">
      <span class="brand-dot"></span>
      <span class="brand-name">Tarnbrook Solar &amp; Electrical</span>
    </header>

    <div class="hero-photo" role="img" aria-label="Photo of an installer kneeling on a roof beside rows of blue solar panels under a clear sky"></div>

    <div class="question-band">
      <h1 class="question">What will your electricity bill<br>look like in 5 years time?</h1>
    </div>

    <h2 class="reasons-title">3 reasons to install solar.</h2>

    <ol class="reasons">
      <li class="reason">1. The sun provides free, clean energy and is the best way to save money.</li>
      <li class="reason">2. The government provides generous incentives saving you thousands of $$.</li>
      <li class="reason">3. Advancing technology means you can store your energy and use it a night.</li>
    </ol>

    <p class="cta">Call us now for a free quote</p>
  </main>
</body>
</html>
```